Upsell Vertical Banner Ad Design For B2B Marketing Agency Vertical 768px × 1180px IS THE SIZE

I need a banner made for my website www.brightlanepromotionhub.biz This banner will be an upsell advertisement for after someone signs up for my monthly program. When they login to their account for the 1st time I will give them the chance to upgrade their account to our annual program with just one click.

this is a page that upsells it currently to give you an idea how we market ourselves:
https://tlpx.pagevault-example.com/page/tlp-annual-upsell

Use this content:

Are You Ready To Commit To Taking Your Business To The Next Level?

Because We're In This For The Long-Haul and Dedicated To Your Success...

Save $300 By Upgrading To An Annual Membership And Pay Only $74/mth

((BUTTON))Yes, Upgrade My Plan Right Now!

*Must prepay the full year at only $898/yr!

Target Market(s)

business owners

Industry/Entity Type

Marketing

Requirements
Must have
• 768px × 1180px IS THE SIZE vertical

Use this content:

Nice to have
• Use this content:

Should not have
• Use this content:

```html
<!DOCTYPE html>
<html lang="en">
<head>
<meta charset="utf-8">
<title>Annual Upgrade Banner</title>
<link rel="stylesheet" href="https://fonts.googleapis.com/css2?family=Arimo:wght@400&family=Oswald:wght@500;700&family=Poppins:wght@400;600&display=swap">
<style>
  :root {
    --stage: #a3a29d;
    --navy-deep: #0e1331;
    --navy-mid: #1d2a56;
    --white: #ffffff;
    --accent-blue: #0519b8;
    --accent-green: #4caf50;
    --cta: #f03a0a;
    --rule: rgba(255,255,255,0.85);
  }
  * { margin: 0; padding: 0; box-sizing: border-box; }
  html, body {
    width: 1200px; height: 1200px; overflow: hidden;
    background: var(--stage);
  }
  .banner {
    position: absolute; left: 243px; top: 53px;
    width: 713px; height: 1094px;
    overflow: hidden;
    color: var(--white);
  }
  .banner__backdrop {
    position: absolute; inset: 0;
    background:
      radial-gradient(ellipse 60% 55% at 50% 48%, var(--navy-mid) 0%, rgba(29,42,86,0) 100%),
      linear-gradient(160deg, #11173a 0%, var(--navy-deep) 100%);
  }
  .banner__corners { position: absolute; inset: 0; width: 713px; height: 1094px; }
  .banner__content { position: absolute; left: 54px; top: 0; right: 54px; }

  .intro {
    position: absolute; top: 95px; left: 0;
    font-family: "Arimo", Arial, sans-serif;
    font-size: 37px; line-height: 63px; font-weight: 400;
    white-space: nowrap;
  }
  .headline {
    position: absolute; top: 258px; left: 0;
    font-family: "Oswald", "Arial Narrow", sans-serif;
    font-weight: 700; font-size: 88px; line-height: 100px;
    letter-spacing: 0.5px; text-transform: uppercase; white-space: nowrap;
  }
  .tagline {
    position: absolute; top: 490px; left: 0;
    font-family: "Poppins", Arial, sans-serif;
    font-size: 22px; line-height: 32px; white-space: nowrap;
  }
  .tagline strong { font-weight: 600; font-size: 26px; }
  .divider {
    position: absolute; top: 524px; left: 0;
    width: 587px; height: 1px; background: var(--rule);
  }
  .offer, .fine-print {
    position: absolute; left: 0;
    font-family: "Oswald", "Arial Narrow", sans-serif;
    font-weight: 500; font-size: 41px; line-height: 51px;
    text-transform: uppercase; white-space: nowrap;
  }
  .offer { top: 575px; }
  .fine-print { top: 892px; }
  .cta {
    position: absolute; top: 775px; left: 0;
    width: 358px; height: 45px;
    background: var(--cta);
    display: flex; align-items: center; justify-content: center;
    font-family: "Poppins", Arial, sans-serif;
    font-size: 21px; color: var(--white); text-decoration: none;
    white-space: nowrap;
  }
</style>
</head>
<body>
  <section class="banner">
    <div class="banner__backdrop" role="img" aria-label="Dark blue tinted photo looking up at city skyscrapers"></div>
    <svg class="banner__corners" viewBox="0 0 713 1094" aria-hidden="true">
      <path d="M0 0 H89 Q45 38 0 59 Z" fill="var(--accent-blue)"/>
      <path d="M615 0 H713 V81 Q655 48 615 0 Z" fill="var(--accent-green)"/>
      <path d="M0 986 Q62 1026 99 1094 H0 Z" fill="var(--accent-green)"/>
      <path d="M713 857 V1094 H502 Q585 928 713 857 Z" fill="var(--accent-blue)"/>
    </svg>
    <div class="banner__content">
      <p class="intro">ARE YOU READY TO<br>COMMIT TO TAKING YOUR</p>
      <h1 class="headline">Business to the<br>next level?</h1>
      <p class="tagline">Because We're In This For The Long-Haul and<br><strong>Dedicated To Your Success...</strong></p>
      <div class="divider"></div>
      <p class="offer">Save $300 by upgrading to an<br>annual membership and pay<br>only $74/ month</p>
      <a class="cta" href="#">Yes, Upgrade My Plan Right Now</a>
      <p class="fine-print">*Must prepay the full<br>year at only&nbsp; $898/year!</p>
    </div>
  </section>
</body>
</html>
```